Tri-fold Brochure Design for Banking Business

The brochure we have needs to be improved - more business like and more attractive. Logo file and brochure is attached. I would like to be able to edit the text after you get done. Your ideas and changes to text are welcome. See our website www.korvanbridgegrp.com for our theme. We can use indesign to edit the text after you complete. However, please make changes to the text we have in the design that it uploaded. Your comments and changes are welcome.

Target Market(s)

Human Resources and learning & development staff at the global investment banks - Pellham Trask, QWNR, etc.

Industry/Entity Type

Investment Banking

Logo Text

Korvan Bridge Group

Font styles to use
Serif
Sans Serif

Colors
33a6d7
0493ce
3277b5
fbf289
fdf9cf
fbee3e
0555a3
85acd3

Requirements
Must have
• Must be similar to our website www.korvanbridgegrp.com. Needs to be business-like, clean fonts, sharp design. Our logo - of course.
Nice to have
• City images - seems to be our theme.

```html
<!DOCTYPE html>
<html lang="en">
<head>
<meta charset="utf-8">
<title>Korvan Bridge Group – Tri-fold Brochure</title>
<link href="https://fonts.googleapis.com/css2?family=Montserrat:wght@400;600;700;800&family=Open+Sans:wght@400;600;700&display=swap" rel="stylesheet">
<style>
:root{
  --navy:#0555a3;
  --blue:#3277b5;
  --sky:#0493ce;
  --cyan:#33a6d7;
  --mist:#85acd3;
  --yellow:#fbee3e;
  --amber:#f6b91c;
  --cream:#fdf9cf;
  --ink:#1d2a3a;
  --grey:#5d6673;
  --paper:#ffffff;
  --backdrop:#e9ecef;
}
*{margin:0;padding:0;box-sizing:border-box}
html,body{width:831px;height:1200px;overflow:hidden;background:var(--backdrop)}
body{position:relative;font-family:"Open Sans",Arial,sans-serif;color:var(--grey)}
.sheet{position:absolute;left:22px;width:787px;display:flex;box-shadow:0 3px 10px rgba(0,0,0,.18);background:var(--paper)}
.sheet--outside{top:18px;height:572px}
.sheet--inside{top:622px;height:566px}
.panel{position:relative;width:262.33px;height:100%;overflow:hidden}
.heading{font-family:"Montserrat",Arial,sans-serif;font-weight:800;text-transform:uppercase;line-height:1.05}
.body-text{font-size:8.6px;line-height:1.55;margin-bottom:9px}
.photo{position:absolute;left:0;width:100%}

/* about */
.about__photo{top:0;height:190px;background:linear-gradient(160deg,#2a4563 0%,#1b2f47 60%,#132336 100%)}
.about__title{position:absolute;top:212px;left:26px;font-size:25px;color:var(--navy)}
.about__title span{color:var(--amber)}
.about__copy{position:absolute;top:258px;left:26px;right:26px}

/* contact */
.contact__title{position:absolute;top:22px;width:100%;text-align:center;font-size:22px;color:var(--navy)}
.contact__title span{color:var(--amber)}
.contact__list{position:absolute;top:58px;width:100%;text-align:center;font-size:7.6px;line-height:1.45;list-style:none}
.contact__list li{margin-bottom:4px}
.contact__list strong{display:block;font-family:"Montserrat",Arial,sans-serif;font-weight:700;color:var(--navy);font-size:7.8px;letter-spacing:.5px}
.contact__photo{top:178px;height:240px;background:linear-gradient(160deg,#3a5878 0%,#24405f 55%,#1a2f48 100%)}
.contact__web{position:absolute;top:444px;left:50%;transform:translateX(-50%);background:var(--yellow);color:var(--ink);font-family:"Montserrat",Arial,sans-serif;font-weight:700;font-size:9.5px;padding:5px 16px;border-radius:12px;white-space:nowrap}
.contact__map{position:absolute;top:476px;left:18px;width:226px;height:64px;border-radius:4px;background:linear-gradient(180deg,#f0f4f8,#dde6ef)}
.contact__tag{position:absolute;bottom:10px;width:100%;text-align:center;font-size:8.5px;color:var(--navy);font-weight:600}

/* cover */
.cover__tag{position:absolute;top:18px;right:22px;font-family:"Montserrat",Arial,sans-serif;font-size:10px;font-weight:700;color:var(--ink)}
.cover__photo{top:40px;height:330px;background:linear-gradient(160deg,#26384f 0%,#142233 55%,#0c1724 100%)}
.cover__brand{position:absolute;top:196px;left:0;width:100%;display:flex;justify-content:center;align-items:center;gap:8px}
.cover__brand-mark{width:12px;height:12px;background:var(--yellow)}
.cover__brand-name{font-family:"Montserrat",Arial,sans-serif;font-weight:700;font-size:15px;letter-spacing:2px;color:var(--paper);text-transform:uppercase}
.cover__title{position:absolute;top:402px;left:0;width:100%;text-align:center;font-size:25px;color:var(--navy)}
.cover__subtitle{position:absolute;top:468px;left:30px;right:30px;text-align:center;font-family:"Montserrat",Arial,sans-serif;font-size:13px;font-weight:600;color:var(--ink);line-height:1.35}

/* why */
.why{background:linear-gradient(180deg,var(--navy) 0%,var(--blue) 100%);color:#e6effa}
.why__title{position:absolute;top:28px;left:24px;font-size:27px;color:var(--paper)}
.why__title span{color:var(--yellow)}
.why__copy{position:absolute;top:100px;left:24px;right:24px}
.why__copy .body-text{color:#d7e5f5}
.why__list{position:absolute;top:198px;left:24px;right:18px;list-style:none}
.why__list li{display:flex;align-items:flex-start;gap:8px;font-size:8.2px;line-height:1.45;margin-bottom:10px;color:#eef4fb}
.why__list svg{flex:none;margin-top:1px;display:block}
.why__photo{bottom:0;height:136px;background:linear-gradient(180deg,#6f93bd 0%,#3f6fa3 100%)}

/* services */
.services__title{position:absolute;top:28px;left:0;width:100%;text-align:center;font-size:27px;color:var(--sky)}
.services__title span{color:var(--amber)}
.services__copy{position:absolute;top:178px;left:26px;right:26px;text-align:center}
.services__copy .body-text{margin-bottom:12px}

/* team */
.team__band{position:absolute;top:0;left:0;width:100%;height:330px;background:var(--yellow)}
.team__title{position:absolute;top:28px;left:24px;font-size:27px;color:var(--ink)}
.team__copy{position:absolute;top:78px;left:24px;right:24px}
.team__copy .body-text{color:#3b3a2a}
.team__cta{font-family:"Montserrat",Arial,sans-serif;font-weight:700;font-size:10px;color:var(--navy);line-height:1.35}
.team__photo{top:330px;height:236px;background:linear-gradient(180deg,#f4d36a 0%,#d9a63c 100%)}
</style>
</head>
<body>

<section class="sheet sheet--outside">
  <article class="panel about">
    <div class="photo about__photo" role="img" aria-label="City skyline photograph"></div>
    <h2 class="heading about__title">About <span>Us</span></h2>
    <div class="about__copy">
      <p class="body-text">Korvan Bridge Group efficiently provides complete sales, marketing and logistical support for all our programs, no matter the location.</p>
      <p class="body-text">Our globally located trainers have extensive experience, both as industry professionals and as trainers.</p>
      <p class="body-text">Our highly qualified logistical team complement the training services, providing reliable and efficient support.</p>
    </div>
  </article>

  <article class="panel contact">
    <h2 class="heading contact__title">Get in <span>Touch</span></h2>
    <ul class="contact__list">
      <li><strong>GLOBAL</strong>global@korvanbridgegrp.com</li>
      <li><strong>ASIA</strong>asia@korvanbridgegrp.com</li>
      <li><strong>UNITED STATES</strong>usa@korvanbridgegrp.com</li>
      <li><strong>EUROPE</strong>europe@korvanbridgegrp.com</li>
    </ul>
    <div class="photo contact__photo" role="img" aria-label="Business district photograph"></div>
    <div class="contact__web">www.korvanbridgegrp.com</div>
    <div class="contact__map" role="img" aria-label="Faint world map"></div>
    <p class="contact__tag">Worldwide Training Service</p>
  </article>

  <article class="panel cover">
    <p class="cover__tag">Worldwide Training Service</p>
    <div class="photo cover__photo" role="img" aria-label="Night city skyline photograph"></div>
    <div class="cover__brand">
      <span class="cover__brand-mark"></span>
      <span class="cover__brand-name">Korvan Bridge</span>
    </div>
    <h1 class="heading cover__title">Business<br>Solutions</h1>
    <p class="cover__subtitle">Your Expert Training and Consulting Partner</p>
  </article>
</section>

<section class="sheet sheet--inside">
  <article class="panel why">
    <h2 class="heading why__title">Why<br>Choose <span>Us?</span></h2>
    <div class="why__copy">
      <p class="body-text">Korvan Bridge Group is dedicated to providing excellent service of the highest standard.</p>
      <p class="body-text">We are dedicated sales and logistics support for every program no matter where it is delivered.</p>
    </div>
    <ul class="why__list">
      <li><svg width="14" height="14" viewBox="0 0 14 14"><circle cx="7" cy="7" r="7" fill="var(--yellow)"/><path d="M4 7.2l2 2 4-4" stroke="var(--navy)" stroke-width="1.6" fill="none"/></svg>Highly qualified, international pool of trainers</li>
      <li><svg width="14" height="14" viewBox="0 0 14 14"><circle cx="7" cy="7" r="7" fill="var(--yellow)"/><path d="M4 7.2l2 2 4-4" stroke="var(--navy)" stroke-width="1.6" fill="none"/></svg>Strong team with deep management support</li>
      <li><svg width="14" height="14" viewBox="0 0 14 14"><circle cx="7" cy="7" r="7" fill="var(--yellow)"/><path d="M4 7.2l2 2 4-4" stroke="var(--navy)" stroke-width="1.6" fill="none"/></svg>Dedicated service and flexibility</li>
      <li><svg width="14" height="14" viewBox="0 0 14 14"><circle cx="7" cy="7" r="7" fill="var(--yellow)"/><path d="M4 7.2l2 2 4-4" stroke="var(--navy)" stroke-width="1.6" fill="none"/></svg>Ability to deliver programs across regions and complex needs</li>
    </ul>
    <div class="photo why__photo" role="img" aria-label="Business team meeting photograph"></div>
  </article>

  <article class="panel services">
    <h2 class="heading services__title">Our<br><span>Services</span></h2>
    <div class="services__copy">
      <p class="body-text">Korvan Bridge Group provides lead in-class services for all our clients.</p>
      <p class="body-text">We provide highly customized programs tailored to your specific requirements.</p>
      <p class="body-text">Direct interaction between our clients, consulting trainers and client services ensures measurable outcomes for program participants.</p>
      <p class="body-text">We facilitate learning outcomes using a blended methodology combining interactive sessions, hands-on experiential models, market simulations and a state of the art learning system.</p>
      <p class="body-text">Our material databases are continuously updated to ensure accuracy and effectiveness of our services.</p>
    </div>
  </article>

  <article class="panel team">
    <div class="team__band"></div>
    <h2 class="heading team__title">Our Team</h2>
    <div class="team__copy">
      <p class="body-text">Our Consulting Trainers are located globally and recognized by the industry as highly effective trainers and program facilitators.</p>
      <p class="body-text">Korvan provides global expertise for our programs with local talent for program delivery.</p>
      <p class="team__cta">Contact us for more information!</p>
    </div>
    <div class="photo team__photo" role="img" aria-label="Smiling consulting team photograph"></div>
  </article>
</section>

</body>
</html>
```